New letter head for Air Conditioning business

We need a new professional letter head design to suit our new re-branded air conditioning business. Our new logo is attached

```html
<!DOCTYPE html>
<html lang="en">
<head>
<meta charset="UTF-8">
<title>Norvent Letterhead</title>
<link rel="stylesheet" href="https://fonts.googleapis.com/css2?family=Open+Sans:wght@400;600;700&display=swap">
<style>
  :root {
    --backdrop: #e8e6e3;
    --paper: #ffffff;
    --ink: #1f1f1f;
    --ink-soft: #4a4a4a;
    --coral: #ec6a5c;
    --coral-light: #f5a79d;
    --silver: #dcdcdc;
    --charcoal: #3b3b3d;
    --brand-green: #4caf72;
    --footer-text: #ffffff;
  }
  html, body {
    margin: 0;
    padding: 0;
    width: 1200px;
    height: 1200px;
    overflow: hidden;
    background: var(--backdrop);
    font-family: "Open Sans", sans-serif;
  }
  .letterhead {
    position: absolute;
    left: 165px;
    top: 40px;
    width: 870px;
    height: 1120px;
    background: var(--paper);
    box-shadow: 0 6px 24px rgba(0,0,0,0.12);
    overflow: hidden;
    color: var(--ink);
  }
  .header-band {
    position: absolute;
    left: 0;
    top: 150px;
    width: 870px;
    height: 22px;
    background: linear-gradient(90deg, var(--coral) 0%, var(--coral-light) 40%, var(--coral) 70%, var(--silver) 100%);
  }
  .footer-band {
    position: absolute;
    left: 0;
    top: 970px;
    width: 870px;
    height: 18px;
    background: linear-gradient(90deg, var(--coral-light) 0%, var(--coral) 50%, var(--silver) 100%);
  }
  .footer {
    position: absolute;
    left: 0;
    top: 988px;
    width: 870px;
    height: 132px;
    background: var(--charcoal);
  }
  .brand {
    position: absolute;
    left: 63px;
    top: 56px;
    display: flex;
    align-items: center;
    gap: 12px;
  }
  .brand__dot {
    width: 34px;
    height: 34px;
    border-radius: 50%;
    background: var(--coral);
  }
  .brand__name {
    font-size: 26px;
    font-weight: 600;
    letter-spacing: 3px;
    color: var(--charcoal);
    line-height: 1;
  }
  .brand__tagline {
    font-size: 6.5px;
    font-weight: 600;
    letter-spacing: 1px;
    color: var(--brand-green);
    text-transform: uppercase;
    margin-top: 4px;
  }
  .block { position: absolute; left: 52px; margin: 0; }
  .label { font-size: 17px; line-height: 1.2; }
  .recipient-name, .sender-name {
    font-size: 15px;
    font-weight: 700;
    line-height: 1.2;
    margin: 0;
  }
  .recipient-role, .sender-role {
    font-size: 12px;
    color: var(--ink-soft);
    line-height: 1.2;
    margin: 0;
  }
  .to { top: 202px; }
  .recipient { top: 230px; }
  .salutation { top: 323px; }
  .date { position: absolute; left: 588px; top: 323px; font-size: 17px; margin: 0; }
  .body-text {
    width: 745px;
    font-size: 14.2px;
    line-height: 20.7px;
  }
  .para-1 { top: 378px; }
  .para-2 { top: 528px; }
  .para-3 { top: 629px; }
  .para-4 { top: 697px; }
  .closing { top: 795px; }
  .sender { top: 853px; }
  .contact {
    position: absolute;
    left: 52px;
    top: 1003px;
    margin: 0;
    padding: 0;
    list-style: none;
    color: var(--footer-text);
    font-size: 12.6px;
  }
  .contact__item {
    display: flex;
    align-items: center;
    gap: 13px;
    height: 26px;
  }
  .contact__icon { width: 19px; height: 19px; flex: none; }
</style>
</head>
<body>
  <main class="letterhead">
    <div class="header-band" role="img" aria-label="Decorative coral and silver wave band"></div>

    <header class="brand">
      <span class="brand__dot"></span>
      <div>
        <div class="brand__name">NORVENT</div>
        <div class="brand__tagline">Air Conditioning &amp; Refrigeration</div>
      </div>
    </header>

    <p class="block label to">To</p>
    <div class="block recipient">
      <p class="recipient-name">LOREM IPSUM</p>
      <p class="recipient-role">dummy text</p>
    </div>

    <p class="block label salutation">Dear,</p>
    <p class="date">Date:</p>

    <p class="block body-text para-1">Lorem Ipsum is simply dummy text of the printing and typesetting industry. Lorem Ipsum has been the industry's standard dummy text ever since the 1500s, when an unknown printer took a galley of type and scrambled it to make a type specimen book. It has survived not only five centuries, but also the leap into electronic typesetting, remaining essentially unchanged. It was popularised in the 1960s with the release of Letraset sheets containing Lorem Ipsum passages, and more recently with desktop publishing software like Aldus PageMaker including versions of Lorem Ipsum.</p>
    <p class="block body-text para-2">Lorem Ipsum is simply dummy text of the printing and typesetting industry. Lorem Ipsum has been the industry's standard dummy text ever since the 1500s, when an unknown printer took a galley of type and scrambled it to make a type specimen book. It has survived not only five centuries, but also the leap into electronic typesetting, remaining essentially unchanged.</p>
    <p class="block body-text para-3">Lorem Ipsum is simply dummy text of the printing and typesetting industry. Lorem Ipsum has been the industry's standard dummy text ever since the 1500s,</p>
    <p class="block body-text para-4">Lorem Ipsum is simply dummy text of the printing and typesetting industry. Lorem Ipsum has been the industry's standard dummy text ever since the 1500s,</p>

    <p class="block label closing">Regards</p>
    <div class="block sender">
      <p class="sender-name">LOREM IPSUM</p>
      <p class="sender-role">dummy text</p>
    </div>

    <div class="footer-band" role="img" aria-label="Decorative coral and silver wave band"></div>
    <div class="footer"></div>

    <ul class="contact">
      <li class="contact__item">
        <svg class="contact__icon" viewBox="0 0 20 20" aria-hidden="true"><circle cx="10" cy="10" r="10" fill="#ec6a5c"/><path d="M6.5,5 L8.5,5 L9.3,7.8 L8,8.8 C8.7,10.4 9.6,11.3 11.2,12 L12.2,10.7 L15,11.5 L15,13.5 C15,14.3 14.3,15 13.5,15 C9.4,14.7 5.3,10.6 5,6.5 C5,5.7 5.7,5 6.5,5 Z" fill="#fff"/></svg>
        <span>1234567890</span>
      </li>
      <li class="contact__item">
        <svg class="contact__icon" viewBox="0 0 20 20" aria-hidden="true"><rect x="0" y="3" width="20" height="14" rx="2" fill="#ec6a5c"/><path d="M1,4.5 L10,11 L19,4.5" fill="none" stroke="#3b3b3d" stroke-width="1.6"/></svg>
        <span>info@norventair.com</span>
      </li>
      <li class="contact__item">
        <svg class="contact__icon" viewBox="0 0 20 20" aria-hidden="true"><circle cx="10" cy="10" r="10" fill="#ec6a5c"/><g fill="none" stroke="#3b3b3d" stroke-width="1.2"><ellipse cx="10" cy="10" rx="4" ry="9"/><line x1="1" y1="10" x2="19" y2="10"/><line x1="10" y1="1" x2="10" y2="19"/><path d="M2.5,5.5 H17.5 M2.5,14.5 H17.5"/></g></svg>
        <span>www.norventair.com</span>
      </li>
      <li class="contact__item">
        <svg class="contact__icon" viewBox="0 0 20 20" aria-hidden="true"><circle cx="10" cy="10" r="10" fill="#ec6a5c"/><path d="M10,4 C7.5,4 6,5.8 6,8 C6,11 10,15.5 10,15.5 C10,15.5 14,11 14,8 C14,5.8 12.5,4 10,4 Z" fill="#fff"/><circle cx="10" cy="8" r="1.6" fill="#ec6a5c"/></svg>
        <span>Lorem Ipsum is simply dummy text of the printing</span>
      </li>
    </ul>
  </main>
</body>
</html>
```